Business is called "Pelton Ledger". Accounting and tax services.

I need a flyer for my new business "Pelton Ledger". I am an individual accountant working for himself on the Sunshine Coast in Queensland Australia. I would like to see designs that communicate reliability and trust. I believe my point of difference is that I am always available to my clients and I will cap my number of clients to ensure I can service them properly. Accountants in general seem to have a bad reputation for not responding to clients in a timely fashion, whether by email or phone. This is where I intend to differentiate myself. I have included my business card for ideas on colour and for contact information. I have also included some logo's that should go on the flyer. With the QLA logo, the words "Pelton Ledger is a QLA Business" needs to be written either above, below or to the right hand side (as per the business card).

Target Market(s)

Small business owners and individuals requiring taxation and financials

Industry/Entity Type

Public Accounting

Font styles to use
Serif

Requirements
Must have
• Supplied logo's, accounting style pictures etc
Services: Small Business Taxation
Company & Trust Tax Returns
Rental Property Returns
Capital Gains Tax
Individual Tax Returns
BAS and IAS lodgements
Nice to have
• Needs to convey a sense of being reliable and responds to clients quickly.
Should not have
• My name

```html
<!DOCTYPE html>
<html lang="en">
<head>
<meta charset="utf-8">
<title>Pelton Ledger – Flyer</title>
<link rel="stylesheet" href="https://fonts.googleapis.com/css2?family=Lato:wght@300;400;700;900&display=swap">
<style>
:root{
  --charcoal:#3e3f41;
  --charcoal-deep:#2f3031;
  --charcoal-mid:#4a4b4d;
  --teal:#52bb9c;
  --teal-deep:#2f9a7b;
  --white:#ffffff;
  --ink:#1d1d1d;
  --muted:#e6e6e6;
}
*{margin:0;padding:0;box-sizing:border-box}
html,body{width:857px;height:1200px;overflow:hidden;background:var(--charcoal)}
.flyer{position:relative;width:857px;height:1200px;overflow:hidden;background:var(--charcoal);font-family:"Lato",sans-serif;color:var(--white)}
.backdrop{position:absolute;inset:0}
.photo{position:absolute;inset:0;clip-path:polygon(215px 0,857px 0,857px 585px,600px 600px,330px 470px,170px 330px);
  background:radial-gradient(ellipse at 62% 42%,#d9d9d9 0%,#a9a9a9 30%,#6f6f6f 62%,#3a3a3a 100%)}
.brand-top{position:absolute;left:118px;top:40px;display:flex;align-items:center;gap:14px}
.brand-top .mark{width:34px;height:34px;border:4px solid var(--teal);border-radius:50%}
.brand-top .name{font-size:26px;font-weight:400;color:var(--teal);letter-spacing:1px}
.headline{position:absolute;left:58px;top:375px;border-left:4px solid var(--teal);padding-left:18px;font-weight:300;font-size:59px;line-height:1.1}
.offer{position:absolute;left:580px;top:360px;width:262px;height:262px;border-radius:50%;background:var(--teal);border:6px solid var(--white);text-align:center;display:flex;flex-direction:column;justify-content:center;align-items:center;color:var(--white)}
.offer .lead{font-size:18px;line-height:1.15}
.offer .big{font-size:66px;font-weight:900;line-height:.95;letter-spacing:1px}
.offer .sub{font-size:22px;font-weight:900;line-height:1.05}
.offer .tail{font-size:15px;line-height:1.15;margin-top:4px}
.tagline{position:absolute;left:56px;top:585px;font-size:31px;font-weight:300;line-height:1.55}
.about{position:absolute;left:60px;top:686px;width:400px;font-size:15px;line-height:1.68;color:var(--muted)}
.services{position:absolute;left:478px;top:640px;list-style:none}
.services h2{font-size:22px;font-weight:700;margin-bottom:4px}
.services li{font-size:23px;font-weight:300;line-height:1.37}
.services li::before{content:"• "}
.services .more{padding-left:20px}
.services .more::before{content:""}
.urgent{position:absolute;left:60px;top:900px;width:460px;font-size:15px;line-height:1.45;color:var(--muted)}
.urgent h3{font-size:16px;font-weight:700;color:var(--white);margin-bottom:2px}
.partners{position:absolute;left:530px;top:912px;display:flex;align-items:center;gap:14px}
.badge-agent{width:42px;height:56px;background:var(--white)}
.qla{display:flex;flex-direction:column;gap:4px}
.qla .row{display:flex;align-items:center;gap:8px}
.qla .square{width:30px;height:30px;background:var(--white)}
.qla .name{font-size:26px;font-weight:400;color:var(--white);line-height:1}
.qla .note{font-size:9.5px;color:var(--white)}
.software{display:flex;align-items:center;gap:6px}
.software .dot{width:14px;height:14px;border-radius:50%;background:var(--white)}
.software .name{font-size:18px;font-weight:400;color:var(--white)}
.footer{position:absolute;left:0;top:997px;width:857px;height:203px;background:var(--teal)}
.footer .brand{position:absolute;left:58px;top:52px;display:flex;align-items:center;gap:24px}
.footer .mark{width:70px;height:70px;border:5px solid var(--ink);border-radius:50%}
.footer .name{font-size:30px;letter-spacing:5px;color:var(--ink);font-weight:400}
.footer .role{position:absolute;left:154px;top:110px;font-size:20px;color:var(--charcoal-deep)}
.contacts{position:absolute;left:552px;top:45px;list-style:none}
.contacts li{display:flex;align-items:center;gap:10px;font-size:20px;height:32px;color:var(--white)}
.contacts svg{width:20px;height:20px;flex:none}
.social{display:inline-flex;gap:5px;margin-left:8px}
.social span{width:17px;height:17px;border-radius:50%;background:var(--white);display:block}
</style>
</head>
<body>
<main class="flyer">
  <svg class="backdrop" width="857" height="1000" viewBox="0 0 857 1000" aria-hidden="true">
    <polygon points="0,0 215,0 170,330 0,250" fill="#333436"/>
    <polygon points="857,520 857,640 700,635" fill="#2f9a7b"/>
    <polygon points="857,640 700,635 857,690" fill="#4a4b4d"/>
  </svg>
  <div class="photo" role="img" aria-label="Black and white photo of two business people shaking hands"></div>

  <div class="brand-top"><span class="mark"></span><span class="name">Pelton Ledger</span></div>

  <h1 class="headline">Got an<br>urgent tax<br>problem?</h1>

  <div class="offer">
    <span class="lead">Call us for<br>a coffee and a</span>
    <span class="big">FREE</span>
    <span class="sub">CONSULTATION</span>
    <span class="tail">and discover a service<br>that is bound to be<br>your cup of tea!</span>
  </div>

  <p class="tagline">Often, time may not be on your side.<br>Fortunately we are.</p>

  <p class="about">From shops, cafes, restaurants and beauty salons to cab drivers, plumbers, electricians, builders and specialist contractors ...and every business in between. We can complete tax returns, calculate any tax liability and advise you on exactly when to make payments and how much to pay.<br>One day you'll discover how to pay less tax. How does today sound?</p>

  <ul class="services">
    <h2>Services:</h2>
    <li>Small Business Taxation</li>
    <li>Company &amp; Trust Tax Returns</li>
    <li>Rental Property Returns</li>
    <li>Capital Gains Tax</li>
    <li>Individual Tax Returns</li>
    <li>BAS and IAS Lodgements</li>
    <li class="more">...and more</li>
  </ul>

  <div class="urgent">
    <h3>Need tax advice urgently?</h3>
    <p>Don't press the panic button, press the phone button and discover an accountancy service that delivers far beyond the numbers.</p>
  </div>

  <div class="partners">
    <div class="badge-agent" role="img" aria-label="Registered tax agent badge"></div>
    <div class="qla">
      <div class="row"><span class="square"></span><span class="name">QLA</span></div>
      <span class="note">Pelton Ledger is a QLA Business</span>
    </div>
    <div class="software"><span class="dot"></span><span class="name">Ledgeo</span></div>
  </div>

  <footer class="footer">
    <div class="brand"><span class="mark"></span><span class="name">PELTON LEDGER</span></div>
    <p class="role">Taxation and Business Accountants</p>
    <ul class="contacts">
      <li><svg viewBox="0 0 20 20"><circle cx="10" cy="10" r="9" fill="none" stroke="#fff" stroke-width="1.5"/><path d="M7 5l2 2-1 1.5c.8 1.6 1.9 2.7 3.5 3.5L13 11l2 2-1.5 1.5C10 14 6 10 5.5 6.5z" fill="#fff"/></svg>0491 572 836<span class="social"><span></span><span></span><span></span></span></li>
      <li><svg viewBox="0 0 20 20"><circle cx="10" cy="10" r="9" fill="none" stroke="#fff" stroke-width="1.5"/><rect x="5.5" y="6" width="9" height="6" fill="none" stroke="#fff" stroke-width="1.4"/><path d="M8 14.5h4M10 12v2.5" stroke="#fff" stroke-width="1.4"/></svg>www.peltonledger.com.au</li>
      <li><svg viewBox="0 0 20 20"><circle cx="10" cy="10" r="9" fill="none" stroke="#fff" stroke-width="1.5"/><rect x="5" y="6.5" width="10" height="7" fill="none" stroke="#fff" stroke-width="1.4"/><path d="M5 6.5l5 4 5-4" fill="none" stroke="#fff" stroke-width="1.4"/></svg>hello@peltonledger.com.au</li>
    </ul>
  </footer>
</main>
</body>
</html>
```